Spiritual Healing bussiness needs logo/business card

Simple, clean looking logo/card
For spiritual business with healing services and occult rituals

Contact Information for Business Card

Needs my name: Tovin Harlowe
Business name: Velka Healing Shop
Services provided and worded in this way:

Reiki Healing
Tarot
Oils
Rituals Of Change

Can look occult like but with light energy.

Colors
0255a3
3276b5
85abd2
33a6d7
85cae6
0292cd

```html
<!DOCTYPE html>
<html lang="en">
<head>
<meta charset="UTF-8">
<title>Velka Healing Shop — Business Card</title>
<link rel="stylesheet" href="https://fonts.googleapis.com/css2?family=Arvo&family=Lato:wght@400;700&display=swap">
<style>
  :root {
    --backdrop: #ece7e0;
    --kraft-light: #e0c198;
    --kraft-mid: #c69a66;
    --kraft-dark: #a87744;
    --ink: #141110;
    --card-shadow: rgba(40, 25, 10, 0.35);
  }
  * { margin: 0; padding: 0; box-sizing: border-box; }
  html, body {
    width: 1200px;
    height: 900px;
    overflow: hidden;
    background: var(--backdrop);
  }
  .canvas {
    position: relative;
    width: 1200px;
    height: 900px;
  }
  .card {
    position: absolute;
    left: 330px;
    width: 557px;
    height: 343px;
    background: linear-gradient(160deg, var(--kraft-light) 0%, var(--kraft-mid) 45%, var(--kraft-dark) 100%);
    box-shadow: 2px 4px 8px var(--card-shadow);
    color: var(--ink);
    text-align: center;
  }
  .card--front { top: 90px; }
  .card--back { top: 469px; }

  .holder-name {
    position: absolute;
    top: 112px;
    left: 0;
    width: 100%;
    font-family: "Lato", sans-serif;
    font-weight: 700;
    font-size: 24px;
    letter-spacing: 0.3px;
  }
  .front-rule {
    position: absolute;
    top: 161px;
    left: 187px;
    width: 180px;
    height: 1px;
    background: var(--ink);
  }
  .contact {
    position: absolute;
    top: 177px;
    left: 0;
    width: 100%;
    font-family: "Lato", sans-serif;
    font-size: 19px;
    line-height: 25px;
  }

  .brand-circle {
    position: absolute;
    top: 66px;
    left: 218px;
    width: 122px;
    height: 122px;
  }
  .shop-name {
    position: absolute;
    top: 196px;
    left: 0;
    width: 100%;
    font-family: "Arvo", serif;
    font-size: 29px;
    letter-spacing: 0.3px;
  }
  .back-rule {
    position: absolute;
    top: 244px;
    left: 86px;
    width: 386px;
    height: 1px;
    background: var(--ink);
  }
  .services {
    position: absolute;
    top: 259px;
    left: 0;
    width: 100%;
    list-style: none;
    display: flex;
    justify-content: center;
    align-items: center;
    font-family: "Lato", sans-serif;
    font-size: 16px;
  }
  .services li + li::before {
    content: "";
    display: inline-block;
    width: 7px;
    height: 7px;
    margin: 0 10px 2px 13px;
    border-radius: 50%;
    background: var(--ink);
  }
</style>
</head>
<body>
<main class="canvas">
  <section class="card card--front" aria-label="Business card front">
    <h1 class="holder-name">TOVIN HARLOWE</h1>
    <div class="front-rule"></div>
    <p class="contact">044-987 210 345<br>hello@velkahealing.com</p>
  </section>

  <section class="card card--back" aria-label="Business card back">
    <svg class="brand-circle" viewBox="0 0 122 122" aria-hidden="true">
      <circle cx="61" cy="61" r="56" fill="none" stroke="var(--ink)" stroke-width="7"/>
    </svg>
    <h2 class="shop-name">Velka Healing Shop</h2>
    <div class="back-rule"></div>
    <ul class="services">
      <li>Reiki Healing</li>
      <li>Tarot</li>
      <li>Oils</li>
      <li>Rituals Of Change</li>
    </ul>
  </section>
</main>
</body>
</html>
```